Asset Mgmt Firm Business Card Design Project

We need a new business card design for our asset management firm. The name of the firm is Meridane CapiLeaf, and the firm is referred to as MCL. We would like to see designs that use blues and greys the business card is to be one-sided. The final design should be conservative to communicate financial safety and growth.

The card must include all of the elements below:

Dominick T. Halvorsen, PhD MBA
Founding Principal

Meridane CapiLeaf Inc
418 Fenwold Street
New York, NY 10482
212-804-3176
dthalvorsen@meridanecapileaf.example
www.meridanecapileaf.example

Our tagline:
"Weighing the risk and return for the future of life sciences"

When designing the business card, please abide by Orlanto Press's guidelines here: http://www.orlantopress.example/op/ns/guide/UploadResources.aspx?selectedTab=0?pfid=088&pf_id=088&xnav=DocSpecs#Bleed

Please use Adobe Illustrator or Adobe Photoshop.

This project has now beenĀ guaranteed.

Best Regards,
Nick

Industry/Entity Type

Asset Management

Requirements
Must have
• logo

white background

```html
<!DOCTYPE html>
<html lang="en">
<head>
<meta charset="utf-8">
<title>Meridane CapiLeaf – Business Card</title>
<link rel="stylesheet" href="https://fonts.googleapis.com/css2?family=Arimo:wght@400&display=swap">
<style>
  :root {
    --navy: #231d63;
    --grey: #7a7a7a;
    --grey-dark: #5e5e5e;
    --tagline: #9a9a9a;
    --card: #ffffff;
    --backdrop: #e6e6e8;
  }
  html, body {
    margin: 0;
    width: 1200px;
    height: 1200px;
    overflow: hidden;
    background: var(--backdrop);
    font-family: "Arimo", Arial, sans-serif;
  }
  .business-card {
    position: absolute;
    left: 75px;
    top: 300px;
    width: 1050px;
    height: 600px;
    background: var(--card);
    box-shadow: 0 6px 24px rgba(0,0,0,0.12);
  }
  .brand {
    position: absolute;
    left: 0;
    right: 0;
    top: 62px;
    display: flex;
    justify-content: center;
    align-items: center;
    gap: 22px;
  }
  .brand-circle {
    width: 70px;
    height: 70px;
    border: 4px solid var(--navy);
    border-radius: 50%;
    box-sizing: border-box;
  }
  .brand-name {
    color: var(--navy);
    font-size: 88px;
    letter-spacing: 14px;
    line-height: 1;
  }
  .tagline {
    position: absolute;
    left: 0;
    right: 0;
    top: 168px;
    margin: 0;
    text-align: center;
    color: var(--tagline);
    font-size: 18px;
  }
  .person {
    position: absolute;
    left: 120px;
    top: 250px;
  }
  .person-name {
    color: var(--navy);
    font-size: 23px;
    margin: 0;
  }
  .person-name .credentials { color: var(--grey-dark); }
  .person-title {
    color: var(--grey-dark);
    font-size: 23px;
    margin: 4px 0 0;
  }
  .divider {
    position: absolute;
    left: 540px;
    top: 300px;
    width: 2px;
    height: 190px;
    background: var(--navy);
  }
  .contact {
    position: absolute;
    left: 568px;
    top: 298px;
    color: var(--grey);
    font-size: 22px;
    line-height: 30px;
  }
  .contact p { margin: 0; }
  .contact .company { color: var(--grey-dark); }
  .contact .line-icon { display: flex; align-items: center; gap: 10px; }
  .contact svg { width: 20px; height: 20px; flex: none; }
  .contact .web-domain { color: var(--navy); }
</style>
</head>
<body>
  <div class="business-card">
    <div class="brand">
      <span class="brand-circle" aria-hidden="true"></span>
      <span class="brand-name">MCL</span>
    </div>
    <p class="tagline">Weighing the risk and return for the future of life sciences</p>

    <div class="person">
      <p class="person-name">Dominick T. Halvorsen<span class="credentials">, PhD MBA</span></p>
      <p class="person-title">Founding Principal</p>
    </div>

    <div class="divider"></div>

    <div class="contact">
      <p class="company">Meridane CapiLeaf Inc</p>
      <p>418 Fenwold Street</p>
      <p>New York, NY 10482</p>
      <p class="line-icon">
        <svg viewBox="0 0 20 20" aria-hidden="true"><circle cx="10" cy="10" r="8.5" fill="none" stroke="#231d63" stroke-width="1.5"/><path d="M7 5.5c-1 1-1 4 1.5 6.5s5.5 2.5 6.5 1.5l-1.6-1.8-1.6.8c-1-.5-2.3-1.8-2.8-2.8l.8-1.6z" fill="#231d63"/></svg>
        212-804-3176
      </p>
      <p class="line-icon">
        <svg viewBox="0 0 20 20" aria-hidden="true"><rect x="1.5" y="4.5" width="17" height="11" fill="none" stroke="#231d63" stroke-width="1.5"/><path d="M1.5 4.5l8.5 6.5 8.5-6.5M1.5 15.5l6-5M18.5 15.5l-6-5" fill="none" stroke="#231d63" stroke-width="1.3"/></svg>
        dthalvorsen@meridanecapileaf.example
      </p>
      <p>www.<span class="web-domain">meridanecapileaf</span>.example</p>
    </div>
  </div>
</body>
</html>
```